Mirela Dawn Business Card Design

I need a business card for my daughter. She has it all described in the file below. But it needs to be square in shape. http://www.mireladawn.example is her web site

Target Market(s)

18-35 year old women

Industry/Entity Type

Fashion

Contact Information for Business Card

Please look at the attached file as it has all the details.

Requirements
Must have
• Please look at the attached file as it has all the details.
Nice to have
Should not have

```html
<!DOCTYPE html>
<html lang="en">
<head>
<meta charset="utf-8">
<title>Mirela Dawn – Business Card</title>
<link rel="stylesheet" href="https://fonts.googleapis.com/css2?family=Yellowtail&family=Mulish:ital,wght@1,300;1,400;1,600&family=Abril+Fatface&display=swap">
<style>
  :root {
    --frame: #161719;
    --pink: #f4a5de;
    --ink: #111214;
    --cream: #fbf8ef;
    --white: #ffffff;
  }
  html, body {
    margin: 0;
    padding: 0;
    width: 1200px;
    height: 1200px;
    overflow: hidden;
    background: var(--frame);
  }
  .card {
    position: relative;
    width: 1200px;
    height: 1200px;
    background: var(--frame);
  }
  .card__panel {
    position: absolute;
    left: 58px;
    top: 56px;
    width: 1086px;
    height: 1088px;
    background: var(--pink);
  }
  .headline {
    position: absolute;
    left: 0;
    width: 1200px;
    top: 112px;
    margin: 0;
    text-align: center;
    font-family: "Yellowtail", cursive;
    font-weight: 400;
    font-size: 104px;
    line-height: 1;
    color: var(--white);
  }
  .tagline {
    position: absolute;
    left: 0;
    width: 1200px;
    top: 282px;
    margin: 0;
    text-align: center;
    font-family: "Yellowtail", cursive;
    font-size: 60px;
    line-height: 1;
    color: var(--white);
  }
  .contacts {
    position: absolute;
    left: 229px;
    top: 418px;
    margin: 0;
    padding: 0;
    list-style: none;
  }
  .contact {
    display: flex;
    align-items: center;
    height: 96px;
    margin-bottom: 18px;
  }
  .contact__badge {
    flex: none;
    width: 92px;
    height: 92px;
    border-radius: 50%;
    background: var(--ink);
    border: 2px solid var(--ink);
    box-shadow: inset 0 0 0 3px var(--pink);
    display: flex;
    align-items: center;
    justify-content: center;
    font-family: "Mulish", sans-serif;
    font-style: italic;
    font-weight: 600;
    font-size: 13px;
    color: var(--cream);
  }
  .contact__badge svg { width: 46px; height: 46px; }
  .contact__text {
    margin-left: 26px;
    font-family: "Mulish", sans-serif;
    font-style: italic;
    font-weight: 400;
    font-size: 46px;
    color: var(--ink);
    white-space: nowrap;
  }
  .links {
    position: absolute;
    left: 188px;
    top: 910px;
    margin: 0;
  }
  .link {
    margin: 0;
    height: 86px;
    white-space: nowrap;
    color: var(--ink);
    font-size: 46px;
  }
  .link__label {
    font-family: "Abril Fatface", serif;
    font-size: 58px;
    letter-spacing: 1px;
  }
  .link__value {
    font-family: "Mulish", sans-serif;
    font-style: italic;
    font-weight: 400;
  }
</style>
</head>
<body>
<main class="card">
  <div class="card__panel"></div>

  <h1 class="headline">Blogger and vlogger</h1>
  <p class="tagline">beauty • fashion • travel</p>

  <ul class="contacts">
    <li class="contact">
      <span class="contact__badge">Pixgram</span>
      <span class="contact__text">pixgram.example/mireladawnxo</span>
    </li>
    <li class="contact">
      <span class="contact__badge">Chirpline</span>
      <span class="contact__text">chirpline.example/mireladawnxo</span>
    </li>
    <li class="contact">
      <span class="contact__badge">Ghostsnap</span>
      <span class="contact__text">@mireladawnxo</span>
    </li>
    <li class="contact">
      <span class="contact__badge">
        <svg viewBox="0 0 48 48" aria-label="Email">
          <rect x="2" y="9" width="44" height="30" rx="2" fill="var(--cream)"/>
          <polyline points="4,12 24,28 44,12" fill="none" stroke="var(--ink)" stroke-width="3.5" stroke-linejoin="round"/>
        </svg>
      </span>
      <span class="contact__text">mirela@mireladawn.example</span>
    </li>
  </ul>

  <div class="links">
    <p class="link"><span class="link__label">Blog</span>: <span class="link__value">mireladawn.example</span></p>
    <p class="link"><span class="link__label">Vlog</span>: <span class="link__value">vidstream.example/mireladawn</span></p>
  </div>
</main>
</body>
</html>
```